Logo & Visitenkarte für ein Ingenieurbüro
Zielgruppe
Ich bin freiberuflich als Ingenieurbüro unterwegs. Projekte, Planungen erneuerbare Energien, Verbrauchsanalysen, Beratungen. Keine spezielle Zielgruppe. Grundthemen: Technik, Menschen, Netzwerk Verbinden
Aufgabenstellung
Das Design soll klar, vertrauensvoll, wertig, sysmpatisch sein.
Grundthemen: Technik, Menschen, Netzwerk, Verbinden
Rückseite: QR-Code von mir kommt dann nach Beratung

```html
<!DOCTYPE html>
<html lang="de">
<head>
<meta charset="utf-8">
<title>Ingenieurbüro Falkenrath – Visitenkarte</title>
<link href="https://fonts.googleapis.com/css2?family=Roboto:wght@300;400;700&display=swap" rel="stylesheet">
<style>
  :root {
    --backdrop: #eceef1;
    --navy-deep: #0c1433;
    --navy: #17234f;
    --map-glow: #2a4a8a;
    --cyan: #5fd3ea;
    --cyan-soft: #8fe3f2;
    --text-light: #d6dcea;
    --text-muted: #9aa6c2;
    --divider: rgba(160, 180, 220, 0.45);
  }
  * { margin: 0; padding: 0; box-sizing: border-box; }
  html, body {
    width: 1200px; height: 719px; overflow: hidden;
    background: var(--backdrop);
    font-family: "Roboto", Arial, sans-serif;
  }
  .canvas {
    position: relative; width: 1200px; height: 719px;
  }
  .card {
    position: absolute; top: 190px;
    width: 520px; height: 336px;
    border-radius: 6px; overflow: hidden;
    background: linear-gradient(135deg, var(--navy) 0%, var(--navy-deep) 100%);
    box-shadow: 0 10px 28px rgba(20, 30, 60, 0.22);
  }
  .card--front { left: 50px; }
  .card--back { left: 630px; }
  .world-network {
    position: absolute; inset: 0;
    background: radial-gradient(ellipse at 55% 45%, rgba(42, 74, 138, 0.55) 0%, rgba(23, 35, 79, 0) 70%);
  }
  .brand-name {
    position: absolute; left: 0; right: 0;
    text-align: center;
    font-weight: 700; color: var(--cyan);
    letter-spacing: 2px;
  }
  .card--front .brand-name { top: 118px; font-size: 40px; }
  .brand-dot {
    display: inline-block; width: 14px; height: 14px;
    background: var(--cyan); margin-right: 12px; vertical-align: 4px;
  }
  .web-tab {
    position: absolute; bottom: 0; left: 145px;
    width: 230px; height: 48px;
    background: var(--cyan);
    border-radius: 12px 12px 0 0;
    display: flex; align-items: center; justify-content: center;
    color: #ffffff; font-size: 19px; font-weight: 400;
  }
  .back-brand {
    position: absolute; left: 60px; bottom: 34px; width: 190px;
    text-align: center;
  }
  .back-brand .name {
    font-size: 26px; font-weight: 700; color: var(--cyan);
    letter-spacing: 1.5px;
  }
  .back-brand .subline {
    margin-top: 6px; font-size: 12px; font-weight: 700;
    color: var(--cyan); letter-spacing: 1.5px;
  }
  .divider {
    position: absolute; left: 268px; top: 60px;
    width: 1px; height: 230px; background: var(--divider);
  }
  .contact {
    position: absolute; left: 290px; top: 48px; width: 220px;
  }
  .contact .person {
    font-size: 25px; font-weight: 400; color: var(--cyan); line-height: 1.1;
  }
  .contact .title {
    font-size: 13px; font-weight: 300; color: var(--text-muted);
    margin-bottom: 14px;
  }
  .contact-row {
    display: flex; align-items: flex-start; gap: 10px;
    margin-bottom: 8px;
    font-size: 12.5px; font-weight: 300; color: var(--text-light); line-height: 1.35;
  }
  .contact-row svg {
    flex: 0 0 14px; width: 14px; height: 14px; margin-top: 1px;
    fill: none; stroke: var(--text-light); stroke-width: 1.4;
  }
</style>
</head>
<body>
<main class="canvas">

  <section class="card card--front">
    <div class="world-network" role="img" aria-label="Weltkarte aus verbundenen Netzwerkpunkten und Linien"></div>
    <div class="brand-name"><span class="brand-dot"></span>FALKENRATH</div>
    <div class="web-tab">www.falkenrath-ing.de</div>
  </section>

  <section class="card card--back">
    <div class="world-network" role="img" aria-label="Weltkarte aus verbundenen Netzwerkpunkten und Linien"></div>

    <div class="back-brand">
      <div class="name">FALKENRATH</div>
      <div class="subline">INGENIEURBÜRO</div>
    </div>

    <div class="divider"></div>

    <div class="contact">
      <div class="person">Jens Falkenrath</div>
      <div class="title">Dipl. Ing. E-Technik</div>

      <div class="contact-row">
        <svg viewBox="0 0 14 14"><path d="M7 13s-4.5-4.6-4.5-7.5a4.5 4.5 0 0 1 9 0C11.5 8.4 7 13 7 13z"/><circle cx="7" cy="5.5" r="1.6"/></svg>
        <div>Brahmsweg 14<br>58520 Bergfelde</div>
      </div>
      <div class="contact-row">
        <svg viewBox="0 0 14 14"><path d="M3 1.5l2 .3 1 3-1.4 1a7 7 0 0 0 3.6 3.6l1-1.4 3 1 .3 2c-.3.8-1.2 1.5-2.2 1.5C5.6 12.5 1.5 8.4 1.5 3.7c0-1 .7-1.9 1.5-2.2z"/></svg>
        <div>02351 - 48 207<br>0171 204 3318</div>
      </div>
      <div class="contact-row">
        <svg viewBox="0 0 14 14"><rect x="1.5" y="3" width="11" height="8" rx="0.8"/><path d="M1.8 3.4L7 7.6l5.2-4.2"/></svg>
        <div>info@falkenrath-ing.de</div>
      </div>
      <div class="contact-row">
        <svg viewBox="0 0 14 14"><circle cx="7" cy="7" r="5.5"/><ellipse cx="7" cy="7" rx="2.4" ry="5.5"/><path d="M1.5 7h11M2.5 4h9M2.5 10h9"/></svg>
        <div>www.falkenrath-ing.de</div>
      </div>
    </div>
  </section>

</main>
</body>
</html>
```